KirvaLume a new start up looking for packaging design for it's organic Cold pressed Peanut oil.

We require a labelling design for a new company based in the UK called ''KirvaLume''. We will be launching Organic cold pressed peanut oil. We would like a design that is simple yet very catchy and not boring.

Target Market(s)
General consumers and healthy eaters, Vegan friendly

Colors
Designer to choose colors to be used in the design.

Must have
• Refer to Packaging document information for labelling.
• Type of bottle 250 ML Tasbel bottle (refer to Bottle Picture doc.)
• Must have the "KirvaLume" logo stamped somewhere on the front of the package (refer to the Logo document)
• Sleek and appetising design
• Neutral colors possible accents with logo colors
• Claims: Organic, Vegan, High in Monounsaturated fat, High in Poly-unsaturated fat(all this in front of the package)
• Made in the uk logo, and EU organic logo
• Social Media Icons (Instagram,Facebook) as well as website (Kirvalume.co.uk)
• Space reserved at the back of the package for barcode and best before date to be printed on.
Be nice to have: picture of the product on the background if possible

Need extra days to review

Target Market(s)

Font styles to use
Serif
Sans Serif
Decorative
Script

Requirements
Must have

• • Refer to Packaging document information for labelling.

```html
<!DOCTYPE html>
<html lang="en">
<head>
<meta charset="utf-8">
<title>KirvaLume Organic Cold Pressed Peanut Oil – Labels</title>
<link href="https://fonts.googleapis.com/css2?family=Montserrat:wght@400;600;700&family=Source+Sans+3:wght@400;600&display=swap" rel="stylesheet">
<style>
  :root {
    --brown: #5a1710;
    --brown-dark: #3f0f0a;
    --cream: #ffffff;
    --backdrop: #e6e7e9;
    --peanut-light: #e9cf9f;
    --peanut-mid: #c98f52;
    --kernel: #b5512a;
  }
  * { margin: 0; padding: 0; box-sizing: border-box; }
  html, body { width: 1200px; height: 1079px; overflow: hidden; }
  body {
    background: var(--backdrop);
    font-family: "Source Sans 3", Arial, sans-serif;
    color: var(--cream);
    position: relative;
  }
  .label {
    position: absolute;
    top: 50px;
    width: 266px;
    height: 980px;
    background: var(--brown);
    box-shadow: 6px 6px 12px rgba(0,0,0,0.25);
    overflow: hidden;
  }
  .label--front { left: 316px; }
  .label--back { left: 614px; }
  .abs { position: absolute; }

  /* Front */
  .front-top { left: 0; top: 0; width: 266px; height: 330px; }
  .brand-name {
    left: 0; width: 266px; top: 78px; text-align: center;
    font-family: "Montserrat", Arial, sans-serif; font-weight: 700;
    font-size: 40px; color: var(--brown-dark);
  }
  .mascot-area {
    left: 93px; top: 145px; width: 80px; height: 140px; border-radius: 40px;
    background: linear-gradient(180deg, #c98f52 0%, #4a1a10 60%, #3a120b 100%);
  }
  .product-name {
    left: 30px; top: 376px;
    font-family: "Montserrat", Arial, sans-serif; line-height: 36px;
  }
  .product-name .light { font-weight: 400; font-size: 23px; display: block; }
  .product-name .bold { font-weight: 700; font-size: 28px; display: block; }
  .claims {
    left: 30px; top: 496px;
    font-family: "Montserrat", Arial, sans-serif; font-size: 14.5px;
    line-height: 19px; font-weight: 400;
  }
  .claims p + p { margin-top: 13px; }
  .badges { left: 28px; top: 614px; width: 210px; height: 64px; }
  .peanuts {
    left: 18px; top: 706px; width: 230px; height: 120px;
    border-radius: 60px 60px 50px 70px;
    background: radial-gradient(ellipse at 55% 45%, var(--kernel) 0%, var(--peanut-mid) 35%, var(--peanut-light) 75%, rgba(233,207,159,0) 100%);
  }
  .made-badge { left: 158px; top: 818px; width: 80px; height: 80px; }
  .volume {
    left: 0; width: 266px; top: 920px; text-align: center;
    font-weight: 600; font-size: 21px;
  }

  /* Back */
  .nutrition-title {
    left: 25px; top: 88px;
    font-family: "Montserrat", Arial, sans-serif; font-weight: 700;
    line-height: 36px;
  }
  .nutrition-title .big { font-size: 37px; display: block; }
  .nutrition-title .sub { font-size: 30px; display: block; }
  .row {
    position: absolute; left: 0; width: 266px;
    display: flex; justify-content: space-between;
    font-size: 18px; padding: 0 22px;
  }
  .row--band { background: var(--cream); color: var(--brown); font-weight: 600; padding: 0 16px 0 26px; height: 26px; align-items: center; }
  .back-text {
    left: 0; width: 266px; text-align: center; font-size: 18px; line-height: 24px;
  }
  .back-text strong { font-weight: 600; }
  .barcode-space { left: 27px; top: 815px; width: 213px; height: 116px; background: var(--cream); }
</style>
</head>
<body>

<section class="label label--front" aria-label="Front label">
  <svg class="abs front-top" viewBox="0 0 266 330" aria-hidden="true">
    <path d="M0 0 H266 V296 H200 Q133 348 66 296 H0 Z" fill="var(--cream)"/>
  </svg>
  <div class="abs brand-name">KirvaLume</div>
  <div class="abs mascot-area" role="img" aria-label="Illustration of a cartoon monkey mascot holding a peanut"></div>

  <h1 class="abs product-name">
    <span class="light">ORGANIC COLD</span>
    <span class="bold">PRESSED</span>
    <span class="bold">PEANUT OIL</span>
  </h1>
  <div class="abs claims">
    <p>HIGH IN<br>MONOUNSATURATED FAT</p>
    <p>HIGH IN<br>POLY-UNSATURATED FAT</p>
  </div>

  <svg class="abs badges" viewBox="0 0 210 64" aria-hidden="true">
    <circle cx="26" cy="30" r="25" fill="none" stroke="var(--cream)" stroke-width="2.5"/>
    <ellipse cx="104" cy="30" rx="30" ry="16" fill="none" stroke="var(--cream)" stroke-width="2" stroke-dasharray="3 5"/>
    <circle cx="184" cy="30" r="25" fill="none" stroke="var(--cream)" stroke-width="2.5"/>
  </svg>

  <div class="abs peanuts" role="img" aria-label="Photograph of opened peanut shells with red-skinned kernels"></div>

  <svg class="abs made-badge" viewBox="0 0 80 80" aria-hidden="true">
    <circle cx="40" cy="40" r="38" fill="#f2f2f2" stroke="#8a8a8a" stroke-width="2"/>
    <circle cx="40" cy="40" r="22" fill="#2b3d7a"/>
  </svg>

  <div class="abs volume">250 ML 8.5 fl.oz</div>
</section>

<section class="label label--back" aria-label="Back label">
  <h2 class="abs nutrition-title">
    <span class="big">NUTRITION</span>
    <span class="sub">INFORMATION</span>
  </h2>

  <div class="row row--band" style="top:183px"><span>Typical values</span><span>per 100g</span></div>
  <div class="row" style="top:222px"><span>Energy</span><span>kJ896/kCal3685</span></div>
  <div class="row row--band" style="top:257px"><span>Fat</span><span>100g</span></div>
  <div class="row" style="top:297px"><span>Of which Saturated</span><span>19.7 g</span></div>
  <div class="row" style="top:336px"><span>Mono-unsaturated</span><span>36.4 g</span></div>
  <div class="row" style="top:376px"><span>Poly-unsaturated</span><span>43.4 g</span></div>
  <div class="row" style="top:411px"><span>Protein</span><span>0.1 g</span></div>
  <div class="row row--band" style="top:443px"><span>Carbohydrate</span><span>&lt;0.5</span></div>
  <div class="row" style="top:478px"><span>Of which sugar &lt;0.1g</span><span></span></div>
  <div class="row" style="top:506px"><span>Fibre</span><span>&lt;0.5</span></div>

  <div class="abs back-text" style="top:562px">
    <strong>INGREDIENTS:</strong><br>100% Organic peanut oil
  </div>
  <div class="abs back-text" style="top:630px">
    <strong>ALLERGY ADVICE:</strong><br>Peanuts are packed on<br>premises that handles<br>cereals, nuts (including<br>peanuts), soya, sesame &amp;<br>products containing gluten.
  </div>

  <div class="abs barcode-space" aria-label="Space for barcode and best before date"></div>
</section>

</body>
</html>
```